Flyer-Design für Grillfleisch Lebensmittelautomat |  BratKammer
Flyer-Design für Grillfleisch Lebensmittelautomat | BratKammer
Zielgruppe
Unsere Marke heißt Bratkammer. Wir betreiben einen SB-Lebensmittelautomaten mit Grillfleisch der heimischen Metzgerei Wendtner aus Erlangen.
Metzgerei Wendtner aus Erlangen:
Kammsteak
Rib Eye
Bauch (mariniert)
Bratwurst
Chili con Carne
Bolognese Sauce
Gulaschsuppe
Wendtner Leberwurst grob
Delikatess Leberwurst
Bratwurstgehäck
Hausmacher Stadtwurst
Beilagen/Grillalternativen
Senf
vegane Brätlinge
Hähnchen
Kräuterbaguette
Olivenmix
Eier aus Franken
Der Standort ist an der FERAX Tankstelle, Lindauer Str. 17.
Bezahlung ausschließlich kontaktlos mit zahlkarte, NORA, PayCircle, Quill Pay, Tandor Pay, cadenza, K Pay, Northern Charge – keine Barzahlung heute möglich
Wir wollen einen ansprechenden hochwertigen Flyer, den wir im Wohngebiet als auch Geschäften und Läden im Umkreis von 2km verteilen wollen. Zielgruppe ist jede Altersgruppe im Umkreis von 2 km mit Interesse am Grillen, sowie regionalen Produkten der Metzgerei Wendtner.
Wir betreiben heute (mehr schlecht als recht) einen Instagram Account „BratKammer“ sowie die Website bratkammer-beispiel.de
Aufgabenstellung
Verwendung des Logos
Angabe der Standorts (auf dem Gelände der FERAX Tankstelle Lindauer Str. 17, Erlangen)
Angabe das Produkte der Metzgerei Wendtner
Schlichtes aber ansprechendes Design mit den Farben des Logos.
Format grundsätzlich egal, ideal wäre aber ein kostengünstiges druckbares Standardformat wie z.B. DIN A6
Es muss auf jeden Fall schnell sichtbar werden, dass wir einen Automaten mit Produkten der Metzgerei Wendtner am Standort FERAX Tankstelle Lindauer Straße 17 betreiben und unseren Kunden regionale Produkte 24/7 anbieten.
Solltet ihr Bilder vom Socialmediaauftritt oder anderes Material von uns benötigen, bitte einfach bei uns melden. Wir haben schonmal Bilder hochgeladen, die uns grundsätzlich gefallen.
Bitte für Bilder von unserem Social Media Auftritt o.ä. direkt anfragen, wir antworten so schnell wir können. Danke!

```html
<!DOCTYPE html>
<html lang="de">
<head>
<meta charset="utf-8">
<title>BratKammer – Flyer Vorder- und Rückseite</title>
<link rel="stylesheet" href="https://fonts.googleapis.com/css2?family=Abril+Fatface&family=Alfa+Slab+One&family=Roboto+Condensed:wght@400;700&display=swap">
<style>
  :root {
    --stage: #bab6b5;
    --brand-red: #d9302c;
    --ink: #111111;
    --white: #ffffff;
    --wood-light: #f2f2f2;
    --wood-mid: #d8d8d8;
    --panel-tint: rgba(205, 205, 205, 0.72);
    --meat-dark: #120d0b;
    --meat-brown: #5a3322;
    --machine-blue: #8aa4c4;
    --machine-dark: #4c6688;
  }
  * { margin: 0; padding: 0; box-sizing: border-box; }
  html, body {
    width: 900px; height: 1200px; overflow: hidden;
    background: var(--stage);
  }
  .stage { position: relative; width: 900px; height: 1200px; }

  /* Front side */
  .flyer-front {
    position: absolute; left: 96px; top: 78px; width: 691px; height: 492px;
    overflow: hidden;
  }
  .front-backdrop {
    position: absolute; inset: 0;
    background: linear-gradient(180deg, var(--wood-light), var(--wood-mid) 50%, var(--wood-light));
  }
  .brand-name {
    position: absolute; left: 0; right: 0; top: 268px;
    text-align: center;
    font-family: "Alfa Slab One", serif;
    font-size: 60px; letter-spacing: 2px; line-height: 1;
    color: var(--ink);
  }
  .brand-mark {
    position: absolute; left: 50%; top: 118px; width: 80px; height: 80px;
    margin-left: -40px; border-radius: 50%;
    background: var(--brand-red);
  }
  .front-tagline {
    position: absolute; left: 0; right: 0; top: 484px; margin-top: -96px;
    text-align: center;
    font-family: "Abril Fatface", serif;
    font-size: 30px; color: var(--brand-red);
  }

  /* Back side */
  .flyer-back {
    position: absolute; left: 96px; top: 626px; width: 691px; height: 490px;
    overflow: hidden;
  }
  .back-photo {
    position: absolute; inset: 0;
    background:
      radial-gradient(ellipse at 50% 45%, var(--meat-brown) 0%, #3a2014 35%, var(--meat-dark) 70%),
      var(--meat-dark);
  }
  .product-panel {
    position: absolute; left: 21px; top: 0; width: 244px; height: 100%;
    background: var(--panel-tint);
  }
  .product-list {
    position: absolute; left: 29px; top: 12px; width: 240px;
    list-style: none;
    font-family: "Abril Fatface", serif;
    font-size: 17.5px; line-height: 23.4px; color: var(--ink);
  }
  .product-list .list-heading { color: var(--brand-red); }
  .product-list .item::before { content: "· "; color: var(--brand-red); }

  .payment-info {
    position: absolute; right: 24px; top: 18px;
    text-align: right;
    font-family: "Roboto Condensed", sans-serif;
    font-size: 14.5px; line-height: 18.5px; color: var(--white);
  }
  .payment-info span { display: block; }

  .vending-machine {
    position: absolute; left: 513px; top: 189px; width: 178px; height: 301px;
    background: linear-gradient(90deg, var(--machine-dark), var(--machine-blue) 40%, var(--machine-blue) 80%, var(--machine-dark));
  }

  .location {
    position: absolute; right: 184px; top: 400px;
    text-align: right;
    font-family: "Roboto Condensed", sans-serif; font-weight: 700;
    font-size: 20px; line-height: 23.5px; color: var(--white);
    text-shadow: 0 0 3px #000, 1px 1px 2px #000;
  }
  .location span { display: block; }
  .location .street { color: var(--brand-red); }
</style>
</head>
<body>
<main class="stage">

  <section class="flyer-front" aria-label="Vorderseite">
    <div class="front-backdrop" role="img" aria-label="Helle, weiß lasierte Holzdielen als Hintergrund"></div>
    <div class="brand-mark" aria-hidden="true"></div>
    <h1 class="brand-name">BRATKAMMER</h1>
    <p class="front-tagline">24/7 für Euch da!</p>
  </section>

  <section class="flyer-back" aria-label="Rückseite">
    <div class="back-photo" role="img" aria-label="Gegrilltes Steak mit Rosmarin und rotem Pfeffer an der Grillgabel über Flammen"></div>
    <div class="product-panel"></div>

    <ul class="product-list">
      <li class="list-heading">Metzgerei Wendtner aus Erlangen:</li>
      <li class="item">Kammsteak</li>
      <li class="item">Rib Eye</li>
      <li class="item">Bauch (mariniert)</li>
      <li class="item">Bratwurst</li>
      <li class="item">Chili con Carne</li>
      <li class="item">Bolognese Sauce</li>
      <li class="item">Gulaschsuppe</li>
      <li class="item">Wendtner Leberwurst grob</li>
      <li class="item">Delikatess Leberwurst</li>
      <li class="item">Bratwurstgehäck</li>
      <li class="item">Hausmacher Stadtwurst</li>
      <li class="list-heading">Beilagen/Grillalternativen</li>
      <li class="item">Senf</li>
      <li class="item">Vegane Brätlinge</li>
      <li class="item">Hähnchen</li>
      <li class="item">Kräuterbaguette</li>
      <li class="item">Olivenmix</li>
      <li class="item">Eier aus Franken</li>
    </ul>

    <p class="payment-info">
      <span>Akzeptierte Zahlungsmittel:</span>
      <span>zahlkarte, NORA, PayCircle,</span>
      <span>Quill Pay, Tandor Pay,</span>
      <span>cadenza, K Pay,</span>
      <span>Northern Charge</span>
    </p>

    <div class="vending-machine" role="img" aria-label="Blauer Lebensmittelautomat mit gefüllten Fächern und Bezahlterminal"></div>

    <p class="location">
      <span>Der Standort ist an der</span>
      <span>FERAX Tankstelle,</span>
      <span class="street">Lindauer Str. 17.</span>
    </p>
  </section>

</main>
</body>
</html>
```